Executive Taxi firm with Chauffeur service Website

I have my domain name registered and I have started to work on my site but I am struggling. I am just about to get a logo for the company and need a web site that clearly represents the fact we are an executive/luxury brand in private hire vehicles. We offer airport transfers, train station transfers, seaport transfers, holiday transfers and business to business pick up and drop off.

Target Market(s)

Corporate people, holidaymakers looking for a luxury start their holiday. VIPs' and celebrities.

Number of Pages Required

5+ page

Font styles to use
Serif
Sans Serif
Decorative
Script

Colors

Designer to choose colors to be used in the design.

Requirements
Must have
• Home Page, Services, About Us, VIP and Contact us
• Please see www.brovencars.co.uk I have started it but not happy with it at all.
Nice to have
• Booking form or enquiry form.

```html
<!DOCTYPE html>
<html lang="en">
<head>
<meta charset="utf-8">
<title>Executive Land Travel</title>
<link rel="stylesheet" href="https://fonts.googleapis.com/css2?family=Catamaran:wght@300;400;500;600;700;800;900&display=swap">
<style>
:root{
  --yellow:#f5cf00;
  --ink:#222222;
  --text:#333333;
  --muted:#8a8a8a;
  --line:#cfcfcf;
  --footer:#3e3e3e;
  --white:#ffffff;
}
*{box-sizing:border-box;margin:0;padding:0}
html,body{width:738px;height:1200px;overflow:hidden;background:var(--white)}
body{font-family:"Catamaran",sans-serif;color:var(--text);position:relative}
.abs{position:absolute}

/* header */
.site-header{position:absolute;left:0;top:0;width:738px;height:52px;background:var(--white)}
.main-nav{position:absolute;left:270px;top:22px;display:flex;gap:20px;font-size:9.5px;color:var(--ink)}
.header-call{position:absolute;left:578px;top:12px;display:flex;gap:8px;align-items:flex-start}
.header-call small{display:block;font-size:5px;letter-spacing:.3px;color:var(--text)}
.header-call strong{display:block;font-weight:400;font-size:12px;color:var(--ink);line-height:1.1}

/* hero */
.hero{position:absolute;left:0;top:52px;width:738px;height:289px;
  background:radial-gradient(ellipse at 80% 30%,#6b5a1a 0%,#3a3320 30%,#1c1c1c 65%),#1b1b1b}
.booking-card{position:absolute;left:62px;top:54px;width:234px;height:196px;background:var(--white);overflow:hidden}
.booking-head{height:32px;background:var(--yellow);display:flex;align-items:center;justify-content:space-between;padding:0 22px}
.booking-head h2{font-size:10.5px;font-weight:600;color:var(--ink)}
.booking-corner{position:absolute;right:0;bottom:0}
.field{position:absolute;width:84px;border-bottom:1px solid var(--line);font-size:6px;color:var(--muted);padding-bottom:3px}
.btn-dark{position:absolute;background:var(--ink);color:var(--yellow);font-size:9px;display:flex;align-items:center;justify-content:center}
.hero-copy{position:absolute;left:369px;top:86px;color:var(--white);line-height:1.1}
.hero-copy .l1{font-size:20px;font-weight:800;color:var(--yellow)}
.hero-copy .l2{font-size:19px;font-weight:300}
.hero-copy .l2 b{font-weight:800;color:var(--yellow)}
.hero-copy .l3{font-size:20.5px;font-weight:900;margin-top:6px}

/* services */
.section-title{position:absolute;left:0;width:738px;top:378px;text-align:center;font-size:16px;font-weight:400;color:var(--ink)}
.section-title b{font-weight:700}
.title-rule{position:absolute;left:344px;top:401px;width:66px;height:2px;background:var(--yellow)}
.service{position:absolute;top:464px;width:150px;text-align:center;font-size:12px;color:var(--ink)}
.service svg{display:block;margin:0 auto 14px}
.divider{position:absolute;top:464px;height:86px;width:0;border-left:1px dashed var(--line)}

/* about band */
.about-band{position:absolute;left:0;top:595px}
.about-photo{position:absolute;left:62px;top:629px;width:307px;height:251px;border:3px solid var(--white);border-radius:8px;
  background:linear-gradient(135deg,#b7b7b4 0%,#8d8a84 45%,#5a5650 100%)}
.about-copy{position:absolute;left:405px;top:655px;width:280px}
.about-copy h3{font-size:16px;font-weight:700;color:var(--ink);margin-bottom:10px}
.about-copy p{font-size:8.4px;line-height:21.6px;color:var(--ink)}

/* call strip */
.call-line{position:absolute;left:0;width:738px;top:950px;text-align:center;font-size:12.5px;font-weight:500;color:var(--ink)}
.call-number{position:absolute;left:262px;top:982px;display:flex;align-items:center;gap:18px;font-size:18.5px;font-weight:300;color:var(--ink)}

/* footer */
.footer-bg{position:absolute;left:0;top:1022px}
.footer-col h4{font-size:12px;font-weight:500;color:var(--white);letter-spacing:.3px}
.footer-menu{position:absolute;left:123px;top:1061px}
.footer-menu ul{list-style:none;margin-top:14px;font-size:9.5px;color:#e6e6e6;line-height:16px}
.footer-news{position:absolute;left:224px;top:1061px;width:160px}
.footer-news p{font-size:8.5px;color:#e6e6e6;margin-top:14px}
.news-input{width:156px;height:22px;background:#5b5b5b;margin-top:8px}
.news-submit{width:57px;height:19px;background:var(--yellow);color:var(--ink);font-size:8.5px;display:flex;align-items:center;justify-content:center;margin-top:8px}
.footer-map{position:absolute;left:450px;top:1053px;width:227px;height:120px;background:linear-gradient(135deg,#4a4a4a,#373737)}
</style>
</head>
<body>

<header class="site-header">
  <nav class="main-nav"><span>Home</span><span>Services</span><span>About</span><span>Contact</span></nav>
  <div class="header-call">
    <svg width="14" height="18" viewBox="0 0 14 18" fill="none" stroke="#444" stroke-width="1"><path d="M3 1 L6 4 L4.5 6.5 C5 9 6.5 11.5 8.5 13 L11 12 L13 15 L10.5 17 C5 15.5 1.5 9 1 3 Z"/></svg>
    <div><small>CALL US ANY TIME :</small><strong>07700 900412</strong></div>
  </div>
</header>

<section class="hero" role="img" aria-label="Night photo of an illuminated taxi roof sign on a yellow cab">
  <form class="booking-card">
    <div class="booking-head">
      <h2>BOOK A RIDE WITH US</h2>
      <svg width="28" height="26" viewBox="0 0 28 26"><rect x="10" y="1" width="8" height="4" fill="#222"/><path d="M5 12 L8 6 H20 L23 12 H26 V21 H2 V12 Z" fill="#222"/><rect x="9" y="8" width="10" height="4" fill="#f5cf00"/><circle cx="7" cy="16" r="2" fill="#f5cf00"/><circle cx="21" cy="16" r="2" fill="#f5cf00"/><rect x="3" y="21" width="5" height="4" fill="#222"/><rect x="20" y="21" width="5" height="4" fill="#222"/></svg>
    </div>
    <div class="field" style="left:21px;top:59px">First Name:</div>
    <div class="field" style="left:127px;top:59px">Last Name:</div>
    <div class="field" style="left:21px;top:86px">Email</div>
    <div class="field" style="left:127px;top:86px">Phone:</div>
    <div class="field" style="left:21px;top:112px">Date</div>
    <div class="field" style="left:127px;top:112px">Time</div>
    <div class="btn-dark" style="left:59px;top:144px;width:104px;height:25px">Submit</div>
    <svg class="booking-corner" width="30" height="62" viewBox="0 0 30 62"><path d="M30 0 V62 H0 C16 50 26 28 30 0 Z" fill="#f5cf00"/></svg>
  </form>
  <div class="hero-copy">
    <div class="l1">PRIVATE HIRE,</div>
    <div class="l2">CHAUFFEUR AND <b>TAXI SERVICE</b></div>
    <div class="l3">EXECUTIVE LAND TRAVEL</div>
  </div>
</section>

<h2 class="section-title"><b>OUR</b> SERVICES</h2>
<div class="title-rule"></div>

<div class="service" style="left:47px">
  <svg width="38" height="36" viewBox="0 0 38 36" fill="none" stroke="#222" stroke-width="1.2"><path d="M8 26 L30 6 C33 3 36 4 34 7 L14 28 Z"/><path d="M20 14 L8 10 L5 12 L16 18"/><path d="M24 20 L28 32 L26 34 L20 23"/><path d="M3 33 L9 27 M1 29 L6 24 M6 35 L11 30"/></svg>
  Airport Transfer
</div>
<div class="divider" style="left:206px"></div>
<div class="service" style="left:207px">
  <svg width="38" height="36" viewBox="0 0 38 36" fill="none" stroke="#222" stroke-width="1.2"><path d="M19 2 V8 M14 8 H24 V13 H14 Z M10 13 H28 V20 H10 Z"/><path d="M4 20 H34 L30 30 H8 Z"/><path d="M1 33 C5 31 8 35 12 33 C16 31 19 35 23 33 C27 31 30 35 37 33"/><circle cx="14" cy="24" r="1"/><circle cx="19" cy="24" r="1"/><circle cx="24" cy="24" r="1"/></svg>
  Seaport&nbsp; Transfer
</div>
<div class="divider" style="left:363px"></div>
<div class="service" style="left:374px">
  <svg width="38" height="36" viewBox="0 0 38 36" fill="none" stroke="#222" stroke-width="1.2"><rect x="9" y="2" width="20" height="26" rx="3"/><rect x="12" y="7" width="14" height="9"/><path d="M19 7 V16 M15 4 H23"/><circle cx="14" cy="22" r="1.5"/><circle cx="24" cy="22" r="1.5"/><path d="M12 28 L7 35 M26 28 L31 35 M10 32 H28"/></svg>
  Train Station&nbsp; Transfer
</div>
<div class="divider" style="left:534px"></div>
<div class="service" style="left:531px">
  <svg width="38" height="36" viewBox="0 0 38 36" fill="none" stroke="#222" stroke-width="1.2"><path d="M19 26 C13 19 10 15 10 10 A9 9 0 0 1 28 10 C28 15 25 19 19 26 Z"/><circle cx="19" cy="10" r="3.5"/><path d="M10 23 H4 L1 34 H37 L34 23 H28 M6 29 H32"/></svg>
  Pick up and Drop off
</div>

<svg class="about-band" width="738" height="318" viewBox="0 0 738 318"><path d="M0 12 C150 -4 300 14 450 8 C580 2 660 10 738 6 V308 C600 300 450 316 300 310 C180 306 80 300 0 312 Z" fill="#f5cf00"/></svg>
<div class="about-photo" role="img" aria-label="Hands holding a smartphone showing a ride booking map on a city street"></div>
<div class="about-copy">
  <h3>Always here for you</h3>
  <p>We provide airport transfers to and from all major UK airports, seaports, train station transfers and an executive business to business transfer service. Whether you have an individual or group transfer request, our company-owned fleet offers a choice of options to suit your needs, from luxury saloons and SUV’s to 9-seat luxury transporters.</p>
</div>
<div class="btn-dark" style="left:402px;top:836px;width:96px;height:29px;font-size:8px">Learn More</div>

<p class="call-line">We are Ready to Take Your Call 24 Hours, 7 Days!</p>
<div class="call-number">
  <svg width="30" height="30" viewBox="0 0 30 30" fill="none" stroke="#333" stroke-width="1.2"><path d="M5 2 L10 7 L7.5 11 C9 15 12 18.5 16 20.5 L20 18 L25 23 L21 27 C11 25 3 16 2 6 Z"/><path d="M17 8 A6 6 0 0 1 22 13 M17 3 A11 11 0 0 1 27 13"/></svg>
  <span>07700 900412</span>
</div>

<svg class="footer-bg" width="738" height="178" viewBox="0 0 738 178"><path d="M0 10 C150 0 300 16 450 6 C580 -2 660 8 738 4 V178 H0 Z" fill="#3e3e3e"/></svg>
<div class="footer-col footer-menu">
  <h4>MENU</h4>
  <ul><li>Home</li><li>Services</li><li>About</li><li>Contact</li></ul>
</div>
<div class="footer-col footer-news">
  <h4>STAY CONNECTED</h4>
  <p>Join our newsletter and find out more.</p>
  <div class="news-input"></div>
  <div class="news-submit">Submit</div>
</div>
<div class="footer-map" role="img" aria-label="Dark street map of the city centre with a location pin"></div>

</body>
</html>
```